The Bramblegate - a start-up Independent Production Company

The creation of a website of which I have examples of sites that I'm looking to mirror almost exactly as well as a rough wireframe(outline of pages - 6 pages) and basic layout vision as well as pictures, info etc. Just looking for someone to put it all together in a professional, creative way. I will also need a header template(letter head) with my company name ( creative lettering with some kind of graphic background) in Microsoft Word that matches the way the name is shown on the website and I will use that Template to print my own letter-head, biz cards, etc. This is ideally a simple job (Trying to keep costs as minimal as possible)

Below are the websites I want to mirror as well as the Wireframe (text/videos incomplete and to be filled in as necessary)

http://quartzlanepictures.net/

http://www.saplinghousetv.com/

http://www.tulbrenfilms.com/

http://www.lanternsmedia.com/

http://www.otterbayproductions.tv/

http://www.brightmorningjoyllc.com/

here is my basic layout vision for the website. ill provide text and pictures. some of the pages will be empty - i can lose them if it'll be less expensive.

The Bramblegate

A Production Company

Home About In Production Programming Clients Client Login Contact

Home

The Bramblegate

A Production Company

The Bramblegate is a full service media production company specializing in non-fiction programming with breakthrough characters and stunning footage. Founded by award-winning producer and 25-year industry veteran Colin Marsh, The Bramblegate utilizes its deep experience in all aspects of the documentary and reality TV world to offer tier-one, Network quality development and production services without the Network headache.

About

xxxxxxxxxxxxxxxxxxxxxxx

In Production

xxxxxxxxxxxxxxxxxxxxxxxx

Programming

xxxxxxxxxxxxxxxxxxxxxxxxx

Clients

xxxxxxxxxxxxxxxxxxxxxxxx

Contact

xxxxxxxxxxxxxxxxxxxxxxxx

```html
<!DOCTYPE html>
<html lang="en">
<head>
<meta charset="utf-8">
<title>The Bramblegate – A Production Company</title>
<link href="https://fonts.googleapis.com/css2?family=Arimo:wght@400;700&display=swap" rel="stylesheet">
<style>
  :root {
    --header-dark: #2b2b2b;
    --band-grey: #e1e1e1;
    --page-white: #ffffff;
    --green: #7d9a2e;
    --green-dark: #5f7526;
    --panel-green-top: #6f8a33;
    --panel-green-bottom: #566b27;
    --nav-bg: #ececec;
    --nav-border: #c9c9c9;
    --text-dark: #333333;
    --text-mid: #8a8a8a;
    --rule-grey: #a9a9a9;
  }
  * { margin: 0; padding: 0; box-sizing: border-box; }
  html, body { width: 1200px; height: 806px; overflow: hidden; background: var(--page-white); }
  body { position: relative; font-family: "Arimo", Helvetica, Arial, sans-serif; color: var(--text-dark); }

  .site-header { position: absolute; left: 0; top: 0; width: 1200px; height: 86px; background: var(--header-dark); }
  .brand { position: absolute; left: 213px; top: 30px; width: 230px; }
  .brand-name { font-weight: 700; font-size: 30px; line-height: 31px; color: var(--green); letter-spacing: -0.5px; white-space: nowrap; }
  .brand-tagline { margin-top: 3px; border-top: 1px solid #ffffff; padding-top: 4px; font-size: 7.5px; letter-spacing: 6.1px; color: #ffffff; text-transform: uppercase; white-space: nowrap; }

  .main-nav { position: absolute; left: 463px; top: 53px; display: flex; height: 33px; }
  .main-nav a { display: flex; align-items: center; justify-content: center; height: 33px; background: var(--nav-bg); border-right: 1px solid var(--nav-border); font-size: 12.5px; color: #555; text-decoration: none; }
  .main-nav a:last-child { border-right: none; }
  .main-nav .caret { margin-left: 9px; width: 7px; height: 5px; }

  .dropdown { position: absolute; left: 525px; top: 95px; width: 114px; height: 82px; background: #fff; box-shadow: 0 1px 4px rgba(0,0,0,.2); padding: 6px 12px 0; z-index: 5; }
  .dropdown a { display: block; font-size: 10px; color: #555; text-decoration: none; height: 25.5px; line-height: 25.5px; border-bottom: 1px solid #e6e6e6; }
  .dropdown a:last-child { border-bottom: none; }

  .hero-band { position: absolute; left: 0; top: 86px; width: 1200px; height: 386px; background: var(--band-grey); }

  .intro-panel { position: absolute; left: 198px; top: 95px; width: 256px; height: 377px; background: linear-gradient(180deg, var(--panel-green-top), var(--panel-green-bottom)); padding: 16px 14px 0 14px; color: #fff; box-shadow: 0 0 12px rgba(0,0,0,.25); }
  .intro-title { font-size: 12.5px; font-weight: 400; margin-bottom: 14px; white-space: nowrap; letter-spacing: -0.2px; }
  .intro-title strong { font-weight: 700; }
  .intro-text { font-size: 9.6px; line-height: 17.1px; text-align: justify; }

  .hero-photo { position: absolute; left: 454px; top: 95px; width: 549px; height: 340px;
    background:
      radial-gradient(ellipse 130px 95px at 72% 62%, rgba(236,234,228,.9), rgba(236,234,228,0) 100%),
      radial-gradient(ellipse 70px 40px at 58% 36%, rgba(70,70,62,.55), rgba(70,70,62,0) 100%),
      radial-gradient(ellipse 60px 90px at 30% 58%, rgba(60,72,88,.45), rgba(60,72,88,0) 100%),
      linear-gradient(180deg, #b29d7a 0%, #a5967a 22%, #8d8a6e 42%, #9a9074 60%, #b7a98c 78%, #a89b80 100%); }
  .slider-arrow { position: absolute; top: 269px; width: 27px; height: 27px; z-index: 3; }
  .slider-arrow.prev { left: 471px; }
  .slider-arrow.next { left: 958px; }

  .film-card { position: absolute; top: 435px; width: 189px; height: 192px; background: #fff; padding: 16px 16px 0; box-shadow: 0 8px 12px -6px rgba(0,0,0,.12); }
  .film-card.muted .film-content { opacity: .55; }
  .film-thumb { width: 157px; height: 90px; }
  .film-title { font-size: 13px; font-weight: 700; color: var(--text-mid); margin-top: 12px; padding-bottom: 9px; border-bottom: 2px solid var(--rule-grey); }
  .film-card.active .film-title { border-bottom-color: var(--green); }
  .film-text { margin-top: 11px; font-size: 10px; line-height: 13.7px; color: var(--text-dark); white-space: nowrap; }

  .footer-rule { position: absolute; left: 198px; top: 668px; width: 805px; height: 2px; background: var(--rule-grey); }
  .social-links { position: absolute; left: 428px; top: 696px; display: flex; gap: 16px; }
  .social-link { width: 56px; height: 56px; border-radius: 50%; background: radial-gradient(circle at 40% 35%, #8cb035, var(--green-dark)); box-shadow: 3px 3px 0 #bdbdbd; display: flex; align-items: center; justify-content: center; color: #fff; font-size: 9.5px; font-weight: 700; text-decoration: none; }
</style>
</head>
<body>
  <header class="site-header">
    <div class="brand">
      <div class="brand-name">the bramblegate</div>
      <div class="brand-tagline">A Production Company</div>
    </div>
    <nav class="main-nav">
      <a href="#" style="width:62px">Home</a>
      <a href="#" style="width:74px">About
        <svg class="caret" viewBox="0 0 7 5"><path d="M0.5 0.5 L3.5 4 L6.5 0.5" fill="none" stroke="#555" stroke-width="1.5"/></svg></a>
      <a href="#" style="width:97px">In Production</a>
      <a href="#" style="width:98px">Programming</a>
      <a href="#" style="width:51px">Clients</a>
      <a href="#" style="width:84px">Client Login</a>
      <a href="#" style="width:74px">Contact</a>
    </nav>
  </header>

  <div class="hero-band"></div>

  <div class="dropdown">
    <a href="#">Our Team</a>
    <a href="#">Our Organization</a>
    <a href="#">Our Mission</a>
  </div>

  <section class="intro-panel">
    <h1 class="intro-title"><strong>The Bramblegate.</strong> A Production Company</h1>
    <p class="intro-text">The Bramblegate is a full service independent media production company specializing in non-fiction programming. Through the expression of narrative, breakthrough characters and world-class footage, The Bramblegate informs, entertains, and moves every audience. Founded by an award-winning producer and 25-year industry veteran, The Bramblegate utilizes its deep knowledge in all aspects of the documentary and reality space to offer tier-one production services. We believe that reality elicits a more visceral reaction than fiction and therefore, our desire for our product is to authenticate and represent our characters in as compelling and captivating manner as we can.</p>
  </section>

  <div class="hero-photo" role="img" aria-label="Film crew loading camera gear beside a white off-road vehicle on a dry scrubby hillside"></div>
  <svg class="slider-arrow prev" viewBox="0 0 27 27"><circle cx="13.5" cy="13.5" r="12.5" fill="#f2f2f2" stroke="#bbb"/><path d="M15.5 8.5 L10.5 13.5 L15.5 18.5" fill="none" stroke="#444" stroke-width="2.2"/></svg>
  <svg class="slider-arrow next" viewBox="0 0 27 27"><circle cx="13.5" cy="13.5" r="12.5" fill="#f2f2f2" stroke="#bbb"/><path d="M11.5 8.5 L16.5 13.5 L11.5 18.5" fill="none" stroke="#444" stroke-width="2.2"/></svg>

  <article class="film-card active" style="left:197px">
    <div class="film-content">
      <div class="film-thumb" role="img" aria-label="Crew filming beside a jungle waterfall" style="background:radial-gradient(ellipse 40px 60px at 78% 55%, rgba(215,222,225,.85), rgba(215,222,225,0)), linear-gradient(90deg,#4a6a2e,#2f4a22 45%,#6d7f5c 65%,#9aa7a0)"></div>
      <h2 class="film-title">Film Title 01</h2>
      <p class="film-text">Lorem ipsum dolor sit amet,<br>omnis euismod indoctum mel.</p>
    </div>
  </article>
  <article class="film-card muted" style="left:403px">
    <div class="film-content">
      <div class="film-thumb" role="img" aria-label="Two pilots in flight suits standing in a hangar" style="background:linear-gradient(180deg,#8c8a7e,#6b6f5c 55%,#5d6150)"></div>
      <h2 class="film-title">Film Title 02</h2>
      <p class="film-text">Lorem ipsum dolor sit amet,<br>omnis euismod indoctum mel.</p>
    </div>
  </article>
  <article class="film-card muted" style="left:609px">
    <div class="film-content">
      <div class="film-thumb" role="img" aria-label="Man on a phone in front of a military helicopter" style="background:radial-gradient(ellipse 35px 50px at 80% 60%, rgba(250,250,250,.95), rgba(250,250,250,0)), linear-gradient(180deg,#c9ccc9,#4f5746 50%,#7a7c6e)"></div>
      <h2 class="film-title">Film Title 03</h2>
      <p class="film-text">Lorem ipsum dolor sit amet,<br>omnis euismod indoctum mel.</p>
    </div>
  </article>
  <article class="film-card muted" style="left:814px">
    <div class="film-content">
      <div class="film-thumb" role="img" aria-label="Crew with gear next to a white vehicle on a dusty hillside" style="background:radial-gradient(ellipse 35px 25px at 72% 62%, rgba(236,234,228,.9), rgba(236,234,228,0)), linear-gradient(180deg,#b29d7a,#8d8a6e 45%,#b7a98c)"></div>
      <h2 class="film-title">Film Title 04</h2>
      <p class="film-text">Lorem ipsum dolor sit amet,<br>omnis euismod indoctum mel.</p>
    </div>
  </article>

  <div class="footer-rule"></div>
  <nav class="social-links">
    <a class="social-link" href="#">Chirper</a>
    <a class="social-link" href="#">Feedline</a>
    <a class="social-link" href="#">Kinfolk</a>
    <a class="social-link" href="#">Boardly</a>
    <a class="social-link" href="#">Orbitus</a>
  </nav>
</body>
</html>
```